Revamp Current Website From 2012 TO 2018

We need a ravamp to our current website. I prefer a professional corporate modern feel to it.

My Current Website is www.brightlanepromoworks.biz. Please redesign the homepage and the /certs page first....see attached document for specific instructions..

There is a lot of content at the bottom but maybe we can shorten that by using titles and a pop up of the details or something so it doesnt take too mcuh space...or maybe a red more hyperlink to see the rest of info in pop up or something or new page...

Target Market(s)

B2B, business owners, website owners, marketing companies.

Industry/Entity Type

Promotional Product

Number of Pages Required

2 page

Colors

Designer to choose colors to be used in the design.

Requirements
Must have
• Please keep in mind logo mock up I am working on that looks beautiful on dark background for header...see attached for logo
• Must use existing content I hope your marketing mind comes in to play when designing the website.
• Must have all my content provided on each page...
Nice to have
• similiar color scheme...
Should not have
• I dont like using templates because usually hard to expand on design in future so Prefer full custom designs
• Please no templates

```html
<!DOCTYPE html>
<html lang="en">
<head>
<meta charset="utf-8">
<title>Brightlane Promoworks – Home</title>
<link href="https://fonts.googleapis.com/css2?family=Lato:wght@400;700;900&family=Roboto:wght@400;500;700&display=swap" rel="stylesheet">
<style>
:root{
  --ink:#2b2f33;
  --dark:#1c1d1f;
  --header:#161718;
  --blue:#0a9be2;
  --blue-light:#29b8f5;
  --blue-deep:#0676c6;
  --sky:#32c2ff;
  --paper:#eeeeee;
  --paper-2:#e2e2e2;
  --grey:#4a4d52;
  --line:#b8babc;
  --white:#ffffff;
}
*{box-sizing:border-box;margin:0;padding:0}
html,body{width:1200px;height:3536px;overflow:hidden}
body{font-family:"Lato",Arial,sans-serif;color:var(--ink);background:var(--paper);position:relative}
section,header,nav,footer{position:absolute;left:0;width:1200px}
.abs{position:absolute}
a{text-decoration:none}

/* header */
.site-header{top:0;height:110px;background:var(--header)}
.brand{left:78px;top:34px;display:flex;align-items:center;gap:12px}
.brand-mark{width:40px;height:40px;background:var(--blue)}
.brand-name{font-family:"Roboto",sans-serif;font-weight:700;font-size:28px;color:var(--blue-light);letter-spacing:.5px}
.phone{top:30px;display:flex;gap:14px;align-items:flex-start;color:var(--white)}
.phone svg{width:44px;height:44px;fill:var(--blue-light)}
.phone small{display:block;font-size:17px;color:#d5d5d5}
.phone strong{display:block;font-family:"Roboto",sans-serif;font-size:28px;font-weight:500}

/* nav */
.main-nav{top:110px;height:72px;background:linear-gradient(var(--blue-light),var(--blue-deep));display:flex;align-items:center;padding-left:78px}
.main-nav a{font-family:"Roboto",sans-serif;color:var(--white);font-weight:700;font-size:17px;height:72px;line-height:72px;padding:0 20px;border-right:1px solid rgba(255,255,255,.35)}
.main-nav a.current{background:#4d4f53;padding:0 22px}

/* hero */
.hero{top:182px;height:573px;background:linear-gradient(#f4f4f4,#dcdcdc)}
.hero-title{top:22px;width:1200px;text-align:center;font-size:27px;font-weight:700;color:#3a3d40;line-height:34px}
.hero-rule{top:96px;left:78px;width:1044px;height:1px;background:#b5b5b5}
.stat{width:134px;height:134px;border-radius:50%;top:118px;border:7px solid #c9cbcd;display:flex;flex-direction:column;align-items:center;justify-content:center;text-align:center;color:var(--white);font-size:16px;line-height:20px;box-shadow:0 0 0 5px #fff inset;padding:0 8px}
.stat b{font-size:21px;font-weight:400;line-height:25px}
.stat.compact{font-size:14px;line-height:17px}
.stat.compact b{font-size:19px;line-height:21px}
.stat.blue{background:var(--blue);border-color:var(--sky)}
.stat.dark{background:#3b3d40;border-color:#7a7c7f}
.btn{display:inline-block;background:linear-gradient(var(--blue-light),var(--blue-deep));color:var(--white);font-weight:700;border-radius:26px;border:3px solid #8bd6fa;text-align:center;font-size:18px}
.hero .btn{left:465px;top:299px;width:270px;height:52px;line-height:46px}
.team-photo{left:78px;top:373px;width:1044px;height:200px;background:linear-gradient(#cdd3da,#8a939e 60%,#3d4652)}

/* welcome */
.welcome{top:755px;height:310px;background:linear-gradient(var(--sky),var(--blue-deep))}
.welcome h1{left:78px;top:52px;font-size:38px;line-height:44px;font-weight:700;color:var(--dark)}
.welcome h1 span{color:var(--white)}
.welcome p{left:78px;top:162px;width:650px;color:var(--white);font-size:15px;line-height:23px}
.laptop-screen{left:790px;top:40px;width:290px;height:190px;background:linear-gradient(135deg,#6d7784,#c4cbd2);border:10px solid #222}
.laptop-base{left:760px;top:230px;width:350px;height:12px;background:#c7cbcf;border-radius:0 0 6px 6px}

/* four ways */
.four-ways{top:1065px;height:810px;background:var(--paper)}
.section-title{width:1200px;text-align:center;font-size:40px;font-weight:700;line-height:48px;color:#2c2e30}
.section-title span{color:var(--blue)}
.four-ways .section-title{top:48px}
.hub{left:497px;top:178px;width:200px;height:200px;border-radius:50%;background:#1b1c1e;border:8px solid var(--blue-light);display:flex;align-items:center;justify-content:center;color:var(--blue-light);font-family:"Roboto",sans-serif;font-weight:700;font-size:26px}
.way{width:280px}
.way h3{font-size:24px;color:var(--blue-deep);font-weight:700;margin-bottom:8px}
.way p{font-size:15px;line-height:22px;color:#555}
.way.right{text-align:right}
.way-icon{width:132px;height:132px;border-radius:50%;background:var(--blue);border:6px solid #bfe6fa;display:flex;align-items:center;justify-content:center}
.way-icon svg{width:62px;height:62px;fill:var(--white)}
.way-num{width:28px;height:28px;border-radius:50%;background:var(--blue);border:2px solid #fff;color:#fff;font-size:14px;text-align:center;line-height:24px}

/* plug in */
.plug-in{top:1875px;height:405px;background:linear-gradient(var(--sky),var(--blue-deep))}
.plug-in .section-title{top:52px;color:var(--dark)}
.model-box{top:251px;width:239px;height:118px;border:2px solid rgba(255,255,255,.55);color:#fff;font-weight:700;font-size:22px;text-align:center;padding-top:72px}
.model-icon{top:192px;width:104px;height:104px;border-radius:50%;background:#3f4144;border:5px solid #d7dadc;display:flex;align-items:center;justify-content:center}
.model-icon svg{width:52px;height:52px;fill:#fff}

/* clients */
.clients{top:2280px;height:301px;background:var(--white)}
.clients .section-title{top:48px}
.client{top:129px;width:239px;height:118px;border:1px solid #d2d2d2;display:flex;align-items:center;justify-content:center;font-weight:700;font-size:22px;color:#2b2f33}

/* promo */
.promo{top:2581px;height:290px;background:linear-gradient(var(--sky),var(--blue-deep))}
.promo-card{top:52px;width:323px;height:188px}
.promo-card.quote{background:#48494c;color:#f2f2f2;font-size:15px;line-height:22px;padding:18px 20px;text-align:center}
.promo-card.photo{display:flex;align-items:flex-start;justify-content:center;padding-top:40px;color:#fff;font-weight:700;font-size:26px;line-height:30px;text-align:center}
.promo-card.p1{background:linear-gradient(#4f5a66,#2a3038)}
.promo-card.p2{background:linear-gradient(#5a6470,#353b42)}

/* offer */
.offer{top:2871px;height:323px;background:var(--white)}
.offer-collage{left:78px;top:40px;width:228px;height:259px;border-radius:50%;background:radial-gradient(circle,#e9d9c4,#c9b59c 60%,#f4f4f4 72%)}
.offer h2{left:370px;top:50px;font-size:38px;line-height:46px;font-weight:700;color:#2c2e30}
.offer h2 span{color:var(--blue)}
.offer .btn{left:370px;top:217px;width:165px;height:52px;line-height:46px}

/* footer */
.site-footer{top:3194px;height:294px;background:var(--header);color:#d8d8d8}
.foot-col{top:40px;font-size:15px;line-height:21px}
.foot-col h4{color:#fff;font-size:20px;font-weight:700;margin-bottom:20px}
.foot-col a{color:#d8d8d8;display:block}
.foot-col .name{color:var(--blue-light)}
.foot-col .row{display:flex;gap:10px;margin-bottom:12px}
.foot-col svg{width:16px;height:16px;fill:#fff;flex:none;margin-top:3px}
.arrow-btn{display:inline-block;width:30px;height:30px;background:#555;margin-right:6px;margin-top:14px}
.arrow-btn svg{width:30px;height:30px;fill:#fff;margin:0}
.legal{top:3488px;height:48px;background:var(--blue-deep);color:#fff;font-size:14px;display:flex;align-items:center;justify-content:space-between;padding:0 78px;white-space:nowrap}
.legal nav a{color:#fff;padding:0 10px;border-left:1px solid #fff}
.legal nav a:first-child{border-left:none}
</style>
</head>
<body>

<header class="site-header">
  <div class="abs brand"><span class="brand-mark"></span><span class="brand-name">Brightlane Promoworks</span></div>
  <div class="abs phone" style="left:585px">
    <svg viewBox="0 0 24 24"><path d="M6.6 10.8a15 15 0 0 0 6.6 6.6l2.2-2.2c.3-.3.7-.4 1-.2 1.1.4 2.3.6 3.6.6.6 0 1 .4 1 1V20c0 .6-.4 1-1 1A17 17 0 0 1 3 4c0-.6.4-1 1-1h3.5c.6 0 1 .4 1 1 0 1.3.2 2.5.6 3.6.1.3 0 .7-.2 1z"/></svg>
    <div><small>USA Office</small><strong>619-555-0142</strong></div>
  </div>
  <div class="abs phone" style="left:865px">
    <svg viewBox="0 0 24 24"><path d="M6.6 10.8a15 15 0 0 0 6.6 6.6l2.2-2.2c.3-.3.7-.4 1-.2 1.1.4 2.3.6 3.6.6.6 0 1 .4 1 1V20c0 .6-.4 1-1 1A17 17 0 0 1 3 4c0-.6.4-1 1-1h3.5c.6 0 1 .4 1 1 0 1.3.2 2.5.6 3.6.1.3 0 .7-.2 1z"/></svg>
    <div><small>International</small><strong>1-800-555-0177</strong></div>
  </div>
</header>

<nav class="main-nav">
  <a class="current" href="#">HOME</a><a href="#">OUR INCENTIVES</a><a href="#">SAMPLES</a><a href="#">HOW IT WORKS</a><a href="#">TESTIMONIALS</a><a href="#">FAQ</a><a href="#">CONTACT</a><a href="#">SIGN UP</a><a href="#" style="border-right:none">LOG IN</a>
</nav>

<section class="hero">
  <h2 class="abs hero-title">Increase Leads &amp; Sales From Your Existing Marketing Efforts By Offering High Perceived<br>Value Incentives To Your Customers!</h2>
  <div class="abs hero-rule"></div>
  <div class="abs stat blue" style="left:91px">12<br>Years In<br>Business</div>
  <div class="abs stat dark" style="left:261px"><b>13,000+</b>Clients<br>Enrolled</div>
  <div class="abs stat blue" style="left:433px"><b>2+ Million</b>Certificates In<br>Circulation</div>
  <div class="abs stat dark" style="left:612px"><b>170,000+</b>Redemptions<br>To Date</div>
  <div class="abs stat blue" style="left:796px"><b>A</b>Rating<br>TrustBureau</div>
  <div class="abs stat dark compact" style="left:972px"><b>Licensed<br>Seller</b>Of Travel CST<br>#4408172</div>
  <a class="abs btn" href="#">30 DAY RISK FREE TRIAL</a>
  <div class="abs team-photo" role="img" aria-label="Photo of a row of smiling business professionals in suits"></div>
</section>

<section class="welcome">
  <h1 class="abs">Welcome To<br><span>Brightlane Promoworks</span></h1>
  <p class="abs">Create a variety giveaway promotions for your business with an unlimited supply of top quality vacation getaway certificates, restaurant gift certificates, electronic product giveaways and gas or grocery rewards for just $99/mth. Whether you need 100 or 100,000 you will never pay more than $99.</p>
  <div class="abs laptop-screen" role="img" aria-label="Laptop showing a business meeting in a conference room"></div>
  <div class="abs laptop-base"></div>
</section>

<section class="four-ways">
  <h2 class="abs section-title">Give Away Unlimited Incentives To Your<br>Customers <span>Four Easy Ways !</span></h2>
  <svg class="abs" style="left:0;top:0" width="1200" height="810" viewBox="0 0 1200 810" fill="none" stroke="#b9bbbd" stroke-width="4">
    <path d="M597 378 V690"/>
    <path d="M567 375 V530 H464"/><path d="M627 375 V530 H735"/>
    <path d="M545 360 V440 H332 V405"/><path d="M649 360 V440 H867 V405"/>
    <path d="M575 560 L471 655"/><path d="M619 560 L726 655"/>
    <g fill="#b9bbbd" stroke="none">
      <circle cx="464" cy="530" r="8"/><circle cx="735" cy="530" r="8"/>
      <circle cx="567" cy="530" r="8"/><circle cx="627" cy="530" r="8"/>
      <circle cx="597" cy="560" r="8"/><circle cx="597" cy="690" r="8"/>
      <circle cx="545" cy="440" r="7"/><circle cx="649" cy="440" r="7"/>
    </g>
  </svg>
  <div class="abs hub">Brightlane</div>

  <div class="abs way right" style="left:102px;top:290px"><h3>Print</h3><p>Download PDF certificates to print and physically hand them out or mail them to your customers!</p></div>
  <div class="abs way" style="left:815px;top:290px"><h3>Email</h3><p>Email e-certificates to your customers individually or in bulk with just one click!</p></div>
  <div class="abs way right" style="left:102px;top:600px"><h3>Online Automation</h3><p>Add our web banners on your website. Your customers click on the banner to get their certificate, 100%...</p></div>
  <div class="abs way" style="left:815px;top:600px"><h3>Sms</h3><p>Send sms-certificates through text messaging with just one click! [[COMING SOON]]</p></div>

  <div class="abs way-icon" style="left:266px;top:406px"><svg viewBox="0 0 24 24"><path d="M7 3h10v4H7zM4 8h16a2 2 0 0 1 2 2v6h-4v4H6v-4H2v-6a2 2 0 0 1 2-2zm4 7v3h8v-3z"/></svg></div>
  <div class="abs way-num" style="left:318px;top:392px">1</div>
  <div class="abs way-icon" style="left:801px;top:406px"><svg viewBox="0 0 24 24"><path d="M3 9l9-6 9 6v11H3zm2 1.5V18h14v-7.5l-7 4.5z"/></svg></div>
  <div class="abs way-num" style="left:853px;top:392px">2</div>
  <div class="abs way-icon" style="left:405px;top:589px"><svg viewBox="0 0 24 24"><path d="M9 2h2l.4 2a6 6 0 0 1 1.6.7l1.7-1.2 1.4 1.4-1.2 1.7c.3.5.5 1 .7 1.6l2 .4v2l-2 .4a6 6 0 0 1-.7 1.6l1.2 1.7-1.4 1.4-1.7-1.2a6 6 0 0 1-1.6.7L11 18H9l-.4-2a6 6 0 0 1-1.6-.7l-1.7 1.2-1.4-1.4 1.2-1.7A6 6 0 0 1 4.4 12L2.4 11.6v-2L4.4 9.2A6 6 0 0 1 5 7.6L3.9 5.9l1.4-1.4L7 5.7a6 6 0 0 1 1.6-.7zm1 5.5A2.5 2.5 0 1 0 10 12a2.5 2.5 0 0 0 0-4.5zM18 14h1.4l.3 1.3 1.1.6 1.2-.5.7 1.2-1 .9v1.2l1 .9-.7 1.2-1.2-.5-1.1.6-.3 1.3H18l-.3-1.3-1-.6-1.3.5-.7-1.2 1-.9v-1.2l-1-.9.7-1.2 1.3.5 1-.6z"/></svg></div>
  <div class="abs way-num" style="left:393px;top:646px">3</div>
  <div class="abs way-icon" style="left:660px;top:589px"><svg viewBox="0 0 24 24"><path d="M3 4h18v12H8l-5 4zm4 4v2h10V8zm0 4v1h7v-1z"/></svg></div>
  <div class="abs way-num" style="left:775px;top:646px">4</div>
</section>

<section class="plug-in">
  <h2 class="abs section-title">We Plug Right Into Your Existing Business Model<br>In 4 Ways:</h2>
  <div class="abs model-box" style="left:78px">Advertising</div>
  <div class="abs model-box" style="left:346px">Residual Business</div>
  <div class="abs model-box" style="left:617px">Sales</div>
  <div class="abs model-box" style="left:886px">Referrals</div>
  <div class="abs model-icon" style="left:145px"><svg viewBox="0 0 24 24"><path d="M3 9h4l9-5v16l-9-5H3zm4 7h3l1 5H8zm12-7a3 3 0 0 1 0 6z"/></svg></div>
  <div class="abs model-icon" style="left:413px"><svg viewBox="0 0 24 24"><circle cx="8" cy="5" r="2.5"/><circle cx="16" cy="5" r="2.5"/><path d="M5 9h6l2 4h-2v9H8v-6H6v6H3v-9zM19 9h-4l-2 4h2v9h3v-9h1z"/></svg></div>
  <div class="abs model-icon" style="left:684px"><svg viewBox="0 0 24 24"><path d="M3 20h18v2H3zm1-4h3v3H4zm5-4h3v7H9zm5-3h3v10h-3zM4 11l5-4 4 3 6-6-1.5-.5H21V8l-.5-1.5L13 13l-4-3-4 3z"/></svg></div>
  <div class="abs model-icon" style="left:953px"><svg viewBox="0 0 24 24"><path d="M1 7h4l3-2h4l-5 4 2 2 4-2 7 6-2 2-1-1-1 1-1-1-1 1-1-1-1 1-4-3H1zm12-2h4l2 2h4v7h-2l-6-5z"/></svg></div>
</section>

<section class="clients">
  <h2 class="abs section-title" style="font-weight:400">Our <span>Clients</span></h2>
  <div class="abs client" style="left:78px">Northgate Realty</div>
  <div class="abs client" style="left:346px">HomeMart Direct</div>
  <div class="abs client" style="left:617px">Velaro Motors</div>
  <div class="abs client" style="left:886px">Skyline Satellite</div>
</section>

<section class="promo">
  <div class="abs promo-card quote" style="left:78px">By adding one extra tagline: "Call for a Free Quote and receive a Three Day Two Night Hotel Stay Certificate to Las Vegas or 50 + other popular destinations, No Purchase Necessary." Imagine how many more leads you could generate.</div>
  <div class="abs promo-card photo p1" style="left:438px" role="img" aria-label="Photo of a resort pool terrace at dusk">Get More New<br>Customers</div>
  <div class="abs promo-card photo p2" style="left:799px" role="img" aria-label="Photo of a city skyline at evening">Increase Repeat &amp;<br>Referral Business</div>
</section>

<section class="offer">
  <div class="abs offer-collage" role="img" aria-label="Collage of happy customers in round frames"></div>
  <h2 class="abs">Give Away An Unlimited Amount Of<br>Certificates To Your Customers<br><span>For Just $99 Bucks A Month.</span></h2>
  <a class="abs btn" href="#">LEARN MORE</a>
</section>

<footer class="site-footer">
  <div class="abs foot-col" style="left:78px">
    <h4>Useful Links</h4>
    <a href="#">Home</a><a href="#">Our Incentives</a><a href="#">Samples</a><a href="#">How It Works</a><a href="#">Testimonials</a><a href="#">Faq</a><a href="#">Contact</a><a href="#">Sign Up</a><a href="#">Log In</a>
  </div>
  <div class="abs foot-col" style="left:349px;width:230px">
    <h4>Client Testimonial</h4>
    <p>I haven't had any negative experiences with restaurant certificates. I love them.</p>
    <p class="name">Marla T.<br>Fort Ridge, AK</p>
    <span class="arrow-btn"><svg viewBox="0 0 24 24"><path d="M14 7l-5 5 5 5z"/></svg></span><span class="arrow-btn"><svg viewBox="0 0 24 24"><path d="M10 7l5 5-5 5z"/></svg></span>
  </div>
  <div class="abs foot-col" style="left:620px;width:240px">
    <h4>Contact Us</h4>
    <div class="row"><svg viewBox="0 0 24 24"><path d="M12 2a7 7 0 0 1 7 7c0 5-7 13-7 13S5 14 5 9a7 7 0 0 1 7-7zm0 4a3 3 0 1 0 0 6 3 3 0 0 0 0-6z"/></svg><span>1480 Harbor Ridge Way<br>Alder Creek,<br>CA 90000<br>CST-4408172</span></div>
    <div class="row"><svg viewBox="0 0 24 24"><path d="M6.6 10.8a15 15 0 0 0 6.6 6.6l2.2-2.2c.3-.3.7-.4 1-.2 1.1.4 2.3.6 3.6.6.6 0 1 .4 1 1V20c0 .6-.4 1-1 1A17 17 0 0 1 3 4c0-.6.4-1 1-1h3.5c.6 0 1 .4 1 1 0 1.3.2 2.5.6 3.6.1.3 0 .7-.2 1z"/></svg><span>USA Office : 619-555-0142</span></div>
    <div class="row"><svg viewBox="0 0 24 24"><path d="M6.6 10.8a15 15 0 0 0 6.6 6.6l2.2-2.2c.3-.3.7-.4 1-.2 1.1.4 2.3.6 3.6.6.6 0 1 .4 1 1V20c0 .6-.4 1-1 1A17 17 0 0 1 3 4c0-.6.4-1 1-1h3.5c.6 0 1 .4 1 1 0 1.3.2 2.5.6 3.6.1.3 0 .7-.2 1z"/></svg><span>International : 1-800-555-0177</span></div>
  </div>
  <div class="abs foot-col" style="left:891px">
    <h4>Hours</h4>
    <p>Mon-Fri 7am - 4pm PST<br>Sat-Sun CLOSED</p>
    <a href="#" style="text-decoration:underline;margin-top:12px">Click Here To Enroll Now</a>
  </div>
</footer>

<div class="abs legal" style="left:0;width:1200px">
  <span><b>© Brightlane Promoworks</b> - 2017. All Rights Reserved.</span>
  <nav style="position:static;width:auto"><a href="#">Affiliate Program</a><a href="#">Terms &amp; Conditions</a><a href="#">Privacy Policy</a></nav>
</div>

</body>
</html>
```